Glimmora Pages with Bold Font

I want the font to be simple yet bold for Glimmora images. Its all about a simple bold readable font. I need a single glimmora page with an image and copy/text on or over the image. The words will change in the future. I'm looking for the right font. I like fiery red and yellow colors. The "One Pic" attached is a sample of what I want without the Veltrix words.

```html
<!DOCTYPE html>
<html lang="en">
<head>
<meta charset="UTF-8">
<title>Glimmora Page – Trainer for Men</title>
<link rel="stylesheet" href="https://fonts.googleapis.com/css2?family=Fira+Sans+Condensed:wght@700&family=Fira+Sans+Extra+Condensed:ital,wght@1,800&display=swap">
<style>
  :root {
    --fire-red-core: #d9262a;
    --fire-red-mid: #b80d12;
    --fire-red-edge: #7e0306;
    --flame-yellow: #f6b800;
    --copy-white: #ffffff;
    --text-shadow: rgba(60, 0, 0, 0.55);
    --skin-light: #e6b08c;
    --skin-deep: #b8754c;
    --hair-gold: #e3c48a;
  }
  * { margin: 0; padding: 0; box-sizing: border-box; }
  html, body {
    width: 1200px;
    height: 1200px;
    overflow: hidden;
    background: var(--fire-red-edge);
  }
  .page {
    position: relative;
    width: 1200px;
    height: 1200px;
    overflow: hidden;
    background: radial-gradient(ellipse 60% 65% at 62% 48%, var(--fire-red-core) 0%, var(--fire-red-mid) 50%, var(--fire-red-edge) 100%);
  }
  .model-photo {
    position: absolute;
    left: 600px;
    top: 28px;
    width: 570px;
    height: 1172px;
    border-radius: 260px 260px 40px 40px;
    background:
      radial-gradient(ellipse 45% 22% at 50% 18%, var(--hair-gold) 0%, rgba(227,196,138,0) 100%),
      linear-gradient(180deg, rgba(230,176,140,0.85) 0%, var(--skin-light) 45%, var(--skin-deep) 100%);
    opacity: 0.9;
    z-index: 1;
  }
  .copy {
    position: absolute;
    left: 88px;
    top: 0;
    z-index: 2;
    white-space: nowrap;
  }
  .brand-line {
    position: absolute;
    top: 104px;
    left: 0;
    font-family: "Fira Sans Condensed", sans-serif;
    font-weight: 700;
    font-size: 40px;
    color: var(--copy-white);
    letter-spacing: 0.2px;
  }
  .headline {
    position: absolute;
    top: 222px;
    left: 0;
    font-family: "Fira Sans Extra Condensed", sans-serif;
    font-style: italic;
    font-weight: 800;
    font-size: 80px;
    line-height: 98px;
    color: var(--flame-yellow);
  }
  .body-copy {
    position: absolute;
    top: 523px;
    left: 0;
    font-family: "Fira Sans Extra Condensed", sans-serif;
    font-style: italic;
    font-weight: 800;
    font-size: 70px;
    line-height: 103px;
    color: var(--copy-white);
    text-shadow: 2px 3px 4px var(--text-shadow);
  }
  .headline span, .body-copy span { display: block; }
</style>
</head>
<body>
  <main class="page">
    <div class="model-photo" role="img" aria-label="Photo of a smiling blonde woman in a white bikini, standing front-on"></div>
    <section class="copy">
      <p class="brand-line">Marla Vey Quinn Trainer for Men</p>
      <h1 class="headline">
        <span>“I feel so used the</span>
        <span>way you seduced me...</span>
        <span>I love it!</span>
      </h1>
      <p class="body-copy">
        <span>Finally got me to</span>
        <span>exercise and it feels</span>
        <span>really great.</span>
        <span>Please seduce me</span>
        <span>anytime.”</span>
      </p>
    </section>
  </main>
</body>
</html>
```